Famous Australian Web Brand (Zentrivo.com.au) Needs a New Website & Logo

Zentrivo.com.au is one of the leading domain name registration businesses in Australia and is looking for an overhaul of its website and brand.

Zentrivo.com.au current products/services include domain name registration, web hosting, web site creation and SSL certificates.

In this design contest on Quorvane, we would like designers to create a new logo and new website design for Zentrivo.com.au.

Here is what contest entrants will need to create:
- 1 new logo
- 1 new home page design
- 1 internal page (pricing page)

The winning designer will receive the main prize of $750. In addition to this, the winning designer will have the opportunity to work with Zentrivo for the build of the full website and may get ongoing design work from Zentrivo.

thank you all for your designs, we are after a web 2.0 look and feel, please dont use serif fonts, lets use modern and sleek ones, i will upload some samples of one we like shortly

header is to be in black with some texturing, white fonts and the call to action buttons are in green.

for the 6 free services, please use round edges for the images with the text under it, as i will upload shortly and we would like custome images, not stockimage types please

im uploading a sample of a background image for the header, which is black with texturing and also and image for the footer/middle of the page which has the correct shading of the grey for the middle section

please see file 8 for the look we are trying to get with our site and for font ideas

Reason: we have decided to extend the contest for another 3 days as a couple of designers have requested a bit more time

Target Market(s)

People that might need to buy a domain name or start a website: small business owners; entrepreneurs; bloggers; everyone from mum-and-dad website owners to tech savvy entrepreneurs. Geographically we will be targeting Australia but this should not influence the design.

Industry/Entity Type

Build

Requirements
Must have
• The logo should:
- Have the text "Zentrivo"
- Be positioned in the top left hand corner of the website
- Be either a wordmark, pictorial or abstract logo. That is, text-only logos are acceptable but we are also interested in receiving logos with a mark to the left that could somehow represents the business that we’re in

The homepage should:
- Feel modern, slick, web2.0
- Have a horizontal menu with 4 menu items: About Us | Contact Us | My Cart | Login
- Include the logo at the top
- Include the content from this Word Document
- Include the rough layout and style from this JPG template layout

The interior page should:
- Have the same look and feel as the home page
- Include the rough layout and style from this JPG attachment
- Include the content from this second Word Document
Nice to have
• - Grey, white and black primary colors
- Buttons that are green or lime green with a web2.0 call to action
- Full-width design (i.e. across the screen like Quorvane)
Should not have
• - Do not include overt Australian references. While we are an Australian business we do not want Australian flags, kangaroos or Barnaby Wollop in our logo or on our website.
- Do not use the current red color scheme in the design. We want to move away from this.

```html
<!DOCTYPE html>
<html lang="en">
<head>
<meta charset="utf-8">
<title>Zentrivo – Domain Names</title>
<link href="https://fonts.googleapis.com/css2?family=Arimo:wght@400;700&display=swap" rel="stylesheet">
<style>
:root{
  --black:#000;
  --ink:#222;
  --text:#333;
  --grey-panel:#e4e4e4;
  --grey-band:#f2f2f2;
  --grey-line:#bdbdbd;
  --nav-dark:#222;
  --field:#3a3a3a;
  --field-end:#2a2a2a;
  --lime-top:#c9df4a;
  --lime-bot:#8fae1b;
  --white:#fff;
  --muted:#c8c8c8;
}
*{margin:0;padding:0;box-sizing:border-box}
html,body{width:1036px;height:1200px;overflow:hidden;background:var(--black)}
body{position:relative;font-family:Arimo,Arial,sans-serif;color:var(--text)}
.abs{position:absolute}
.header-texture{left:480px;top:0;width:556px;height:280px;
  background:radial-gradient(ellipse at 70% 30%,#3a3a3a 0%,#1a1a1a 45%,transparent 75%)}
.top-nav{left:608px;top:0;width:268px;height:36px;background:var(--nav-dark);display:flex;align-items:center;justify-content:center;gap:8px;font-size:11px;font-weight:700;color:var(--white)}
.top-nav span.sep{color:var(--white)}
.phone-top{right:161px;top:48px;color:var(--white);font-weight:700;font-size:14px}
.logo{left:185px;top:50px;display:flex;align-items:center;gap:10px}
.logo-square{width:44px;height:44px;background:var(--lime-top)}
.logo-name{font-size:40px;color:var(--white);font-weight:400;letter-spacing:-0.5px}
.hero-title{left:185px;top:175px;color:var(--white);font-weight:700;font-size:15px}
.search{left:183px;top:199px;width:315px;height:30px;display:flex;border:1px solid #555}
.search .pre,.search .suf{background:#2c2c2c;color:#ddd;font-size:10px;display:flex;align-items:center;padding:0 7px}
.search .field{flex:1;background:linear-gradient(var(--field),var(--field-end));border-left:1px solid #555;border-right:1px solid #555}
.search-links{left:186px;top:236px;display:flex;gap:14px;align-items:center;font-size:11px;color:var(--muted)}
.dot{width:4px;height:4px;border-radius:50%;background:#aaa}
.panel{left:159px;top:312px;width:724px;height:771px;background:var(--grey-panel);border-radius:6px}
.tab{top:292px;width:133px;height:48px;background:#f5f5f5;border-radius:6px 6px 0 0;padding:6px 4px 0}
.tab-btn{height:30px;border-radius:3px;background:linear-gradient(var(--lime-top),var(--lime-bot));color:var(--white);font-size:14px;display:flex;align-items:center;justify-content:center}
.dropdown{left:179px;top:333px;width:133px;background:#d6d6d6;border-radius:0 0 6px 6px;box-shadow:0 2px 3px rgba(0,0,0,.15)}
.dropdown li{list-style:none;height:24px;line-height:24px;padding-left:8px;font-size:11px;color:#555;border-bottom:1px solid #eee}
.video{top:361px;height:91px;border-radius:3px;background:linear-gradient(#2e2e2e,#555);}
.video-play{position:absolute;left:50%;top:50%;width:26px;height:26px;margin:-13px 0 0 -13px;border-radius:50%;background:rgba(180,210,60,.85)}
.video-play::after{content:"";position:absolute;left:10px;top:7px;border-left:9px solid #fff;border-top:6px solid transparent;border-bottom:6px solid transparent}
.caption{top:460px;font-size:10px;color:var(--ink);line-height:11px}
.band{left:159px;top:492px;width:724px;height:83px;background:var(--grey-band)}
.tagline{left:315px;top:511px;font-size:20px;color:#333;line-height:22px}
.card-img{width:193px;height:116px;border-radius:8px;border:1px solid #999}
.card-title{font-size:11px;font-weight:700;color:var(--ink)}
.card-text{width:194px;font-size:10px;line-height:14.3px;text-align:justify;color:var(--text)}
.vline{width:1px;background:var(--grey-line)}
.footer-nav{left:165px;top:1104px;display:flex;gap:8px;color:var(--white);font-size:11px;font-weight:700}
.legal{left:161px;top:1157px;color:var(--white);font-size:10px}
.contact-box{left:718px;top:1103px;width:165px;height:66px;border:1px solid var(--white);color:var(--white);text-align:center;font-size:11px;padding-top:10px;line-height:13px}
.contact-box strong{display:block}
.contact-box .num{margin-top:8px;font-weight:700}
</style>
</head>
<body>
<div class="abs header-texture" role="img" aria-label="Dark textured pixel grid backdrop"></div>

<nav class="abs top-nav"><span>About Us</span><span class="sep">|</span><span>Contact Us</span><span class="sep">|</span><span>My Cart</span><span class="sep">|</span><span>Login</span></nav>
<div class="abs phone-top">1300 42 71 90</div>

<div class="abs logo"><div class="logo-square"></div><div class="logo-name">Zentrivo</div></div>

<h1 class="abs hero-title">You get a lot more than just a domain name</h1>
<div class="abs search"><span class="pre">www.</span><span class="field"></span><span class="suf">com</span></div>
<div class="abs search-links"><span>Renew a domain</span><span class="dot"></span><span>Transfer a domain</span><span class="dot"></span><span>View Price List</span></div>

<div class="abs panel"></div>
<div class="abs tab" style="left:179px"><div class="tab-btn">Domains</div></div>
<div class="abs tab" style="left:316px"><div class="tab-btn">Creator</div></div>
<div class="abs tab" style="left:453px"><div class="tab-btn">Email</div></div>
<div class="abs tab" style="left:590px"><div class="tab-btn">Hosting</div></div>
<div class="abs tab" style="left:726px"><div class="tab-btn">Marketing</div></div>
<ul class="abs dropdown"><li>Register Domains</li><li>Transfer Domains</li><li>Renew Domains</li><li>Name Servers</li></ul>

<div class="abs video" style="left:308px;width:117px" role="img" aria-label="Video still: man working at a computer"><span class="video-play"></span></div>
<div class="abs video" style="left:466px;width:116px" role="img" aria-label="Video still: presenter in an office"><span class="video-play"></span></div>
<div class="abs video" style="left:619px;width:121px" role="img" aria-label="Video still: presenter beside a list slide"><span class="video-play"></span></div>
<p class="abs caption" style="left:309px">Everyone needs a<br>domain name</p>
<p class="abs caption" style="left:466px">How you can use a<br>domain name</p>
<p class="abs caption" style="left:619px">Why choose<br>Zentrivo</p>

<div class="abs band"></div>
<p class="abs tagline">Everything your business needs to be successful<br>online is <strong>FREE</strong> with every domain name.</p>

<div class="abs vline" style="left:412px;top:588px;height:228px"></div>
<div class="abs vline" style="left:627px;top:588px;height:228px"></div>
<div class="abs" style="left:208px;top:825px;width:624px;height:1px;background:var(--grey-line)"></div>
<div class="abs vline" style="left:412px;top:838px;height:232px"></div>
<div class="abs vline" style="left:627px;top:838px;height:232px"></div>

<div class="abs card-img" style="left:208px;top:583px;background:linear-gradient(135deg,#3a6fa8,#c06a2a 50%,#2c8a3a)" role="img" aria-label="Collage of website templates"></div>
<h3 class="abs card-title" style="left:211px;top:710px">Free 15 Page Website</h3>
<p class="abs card-text" style="left:210px;top:729px">Create a professional, full-featured website in minutes without any technical knowledge. Choose from 4,000+ stunning website designs and customize your site with near-limitless options. Upload your own artwork for a truly personalised look.</p>

<div class="abs card-img" style="left:424px;top:583px;background:linear-gradient(#3d6fd0,#e8eef8 30%,#f4f4f4)" role="img" aria-label="Screenshot of an email program"></div>
<h3 class="abs card-title" style="left:426px;top:710px">Free Professional Email</h3>
<p class="abs card-text" style="left:426px;top:729px">Having a personalised address that matches your domain name (for example, Tom@TomsMuffins.com or Sales@TomsMuffins.com) gives your company a much more professional image when you communicate with customers and associates.</p>

<div class="abs card-img" style="left:640px;top:583px;background:linear-gradient(#6aa6d8,#eef3f8 35%,#f7f7f7)" role="img" aria-label="Screenshot of a hosted web page"></div>
<h3 class="abs card-title" style="left:644px;top:708px">Free Website Hosting</h3>
<p class="abs card-text" style="left:640px;top:728px">We provide the fast and secure hosting for your website. We take care of all the maintenance so all you have to do is create content for your site. Best of all, you don't have to pay a cent for hosting for as long as your domain is registered with us.</p>

<div class="abs card-img" style="left:206px;top:835px;background:linear-gradient(135deg,#cfd8e4,#8aa2c2 60%,#e4e8ee)" role="img" aria-label="Magnifying glass over a search results page"></div>
<h3 class="abs card-title" style="left:210px;top:963px">Free Search Engine Optimisation</h3>
<p class="abs card-text" style="left:210px;top:983px">What good is the best looking website if no one visits it? We thought about that too! All our sites are optimised for search engines by default to ensure that your website is found by Findora and other search engines like Yelko and Scoutly.</p>

<div class="abs card-img" style="left:423px;top:835px;background:linear-gradient(135deg,#7a9ab0,#4a5560 55%,#c9d3da)" role="img" aria-label="Support agent wearing a headset"></div>
<h3 class="abs card-title" style="left:426px;top:963px">Free Business Class Support</h3>
<p class="abs card-text" style="left:426px;top:983px">This is a point of pride for us and we are here to help. We're available to you 24 hours a day, everyday. Many of our competitors don't even provide a phone number for you to call! You deserve the best, and we won't settle for providing anything less.</p>

<div class="abs card-img" style="left:639px;top:835px;background:linear-gradient(135deg,#8a9a6a,#c9c2a0 50%,#5a6040)" role="img" aria-label="Hands counting banknotes"></div>
<h3 class="abs card-title" style="left:645px;top:963px">Guaranteed renewal price.</h3>
<p class="abs card-text" style="left:644px;top:983px">You'll never pay more to renew your domain name than the rate you paid when you initially registered it, or what our registration rate was when you transferred. (The only exceptions would be if you took advantage of a limited-time, special price)</p>

<nav class="abs footer-nav"><span>About Us</span><span>|</span><span>Contact Us</span><span>|</span><span>My Cart</span><span>|</span><span>Login</span></nav>
<p class="abs legal">2010 zentrivo.com. Tout droits reservés. Site créé par Vantelle 2010 créateur de boutique en ligne Korvash</p>
<div class="abs contact-box">HAVE A QUESTION FOR US?<strong>CONTACT US</strong><div class="num">1300 42 71 90</div></div>
</body>
</html>
```